"Corporate Site Design of Cloud Application Venture"(Wordpress Design Project)

This task is new corporate site design for start-up.
Our company name is "Brindova."
Brindova is a cloud service for users who want to bring their software and settings on multiple computers.
Current beta service page is http://demo.brindova.net . But, now it is not available.
We suggest sample sites below. But, we don't want to follow there. We need you to focus our logo and our company will serve stable service.
http://www.quorvahub.net/design/624957/wordpress-design-by-pelmarix
http://www.quorvahub.net/design/637866/wordpress-design-by-tk
http://www.quorvahub.net/design/613671
http://www.quorvahub.net/design/555672
http://www.quorvahub.net/design/538594
http://www.quorvahub.net/design/544859
http://www.tavinor.net/portfolio/glimbrek/
http://layoutmarsh.net/item/design-company-site/96308
http://www.yorbitstudio.net/images/corporate-dl-thumb.jpg
http://www.vendorquay.net/product-tp/110085749/web_site_design_company.html
(1)we have already had logo-design and please must use it (attached).
we have attached 2 files.
Essential : brindova.ai
voluntary : brindovaicon.ai
(2)Unfortunately, we have no idea now, so depend on you about color, lay-out and something, but we wish people feel deeply impressive when they get our website.
(3)Only if you want to use phrase of my service, please use “Where there is Brindova, there’s your workspace.” (if the English grammar is not correct, please modify it.)
(4)The final design should look modern and sophisticated.
(5)Must have these contents.
In header.
- logo and facebook page link.(http://www.friendlattice.net/brindova)
In Header Menu.
- Top Page (has several news release)
- "News Release" List and News Release Page
- "About Service"
- "About Us"
- "Contact"
And footter has several links.
ex. News release, about service, about us, contact, hiring and so on.

```html
<!DOCTYPE html>
<html lang="en">
<head>
<meta charset="utf-8">
<title>Brindova — Where there is Brindova, there’s your workspace</title>
<link rel="stylesheet" href="https://fonts.googleapis.com/css2?family=Source+Sans+3:wght@300;400;600&family=Ubuntu:wght@500&display=swap">
<style>
:root{
  --brand:#1592d2;
  --brand-dark:#0c6fa8;
  --ink:#1e1e1e;
  --muted:#555;
  --line:#bdbdbd;
  --frame:#a9a9a9;
  --btn:#1c1c1c;
  --bg:#ffffff;
}
*{margin:0;padding:0;box-sizing:border-box}
html,body{width:1193px;height:1200px;overflow:hidden;background:var(--bg)}
body{position:relative;font-family:"Source Sans 3",sans-serif;color:var(--ink)}
.abs{position:absolute}

/* header */
.brand{left:158px;top:78px;display:flex;align-items:center;gap:10px}
.brand-dot{width:16px;height:16px;border-radius:50%;background:var(--brand)}
.brand-name{font-family:"Source Sans 3",sans-serif;font-weight:600;font-size:48px;color:var(--brand);letter-spacing:-1px;line-height:1}
.nav-home{left:401px;top:124px;width:61px;height:19px;border:1px solid #999;font-size:16px;color:#888;text-align:center;line-height:17px}
.nav-link{top:124px;font-size:17px;color:var(--brand);text-decoration:underline;line-height:19px}
.social-square{left:863px;top:123px;width:20px;height:19px;background:#3b5b98}
.search{left:888px;top:123px;width:124px;height:20px;border:1px solid #b5b5b5;font-size:11px;font-weight:600;padding-left:6px;line-height:18px;color:#222}
.search svg{position:absolute;right:6px;top:3px}

/* hero */
.hero-visual{left:196px;top:220px;width:457px;height:315px;border-radius:40px;
  background:radial-gradient(ellipse at 55% 45%,#9fc4e4 0%,#d7e4ee 45%,rgba(255,255,255,0) 72%)}
.arrow{top:334px}
.hero-title{left:664px;top:226px;font-family:"Ubuntu",sans-serif;font-weight:500;font-size:24px;color:var(--brand);text-decoration:underline;text-decoration-thickness:2px;letter-spacing:.2px}
.hero-sub{left:664px;top:256px;font-size:24px;font-weight:400;letter-spacing:.3px}
.hero-copy{left:664px;top:299px;font-size:14.5px;line-height:21px}
.btn{display:flex;align-items:center;background:linear-gradient(#3a3a3a,var(--btn));color:#fff;border-radius:2px;box-shadow:0 3px 5px rgba(0,0,0,.25)}
.btn-large{left:665px;top:406px;width:148px;height:41px;font-size:20px;font-weight:300;gap:14px;padding-left:12px}
.dots{left:565px;top:510px;display:flex;gap:9px}
.dot{width:9px;height:9px;border-radius:50%;background:#bbb;box-shadow:inset 0 1px 2px rgba(0,0,0,.3)}
.dot.active{background:var(--brand)}
.band{left:140px;width:913px;height:60px;background:radial-gradient(ellipse at 50% 100%,#dcdcdc 0%,rgba(255,255,255,0) 70%)}
.band-line{left:170px;width:853px;height:1px;background:linear-gradient(90deg,rgba(200,200,200,0),#bbb,rgba(200,200,200,0))}

/* features */
.feature-title{top:652px;font-size:15px;font-weight:600;color:var(--brand);text-decoration:underline}
.feature-frame{top:690px;width:238px;height:125px;border:2px solid var(--frame);background:#fff;padding:6px}
.feature-art{width:100%;height:100%;background:radial-gradient(ellipse at 50% 50%,#c9d6e2 0%,#eef2f5 60%,#fff 100%)}
.connector{top:779px;height:2px;background:#ccc}
.feature-text{font-size:14.5px;font-weight:300;line-height:18px;color:#333;width:240px}
.btn-small{top:900px;width:74px;height:21px;font-size:10px;gap:6px;padding-left:5px}

.lead{left:175px;top:964px;width:880px;font-size:14.5px;font-weight:300;line-height:18px;color:#333}

/* footer */
.copyright{left:177px;top:1112px;font-size:15px}
.footer-links{right:169px;top:1112px;font-size:15px;text-align:right;line-height:18px}
</style>
</head>
<body>

<header>
  <div class="abs brand"><span class="brand-name">brindova</span><span class="brand-dot"></span></div>
  <div class="abs nav-home">Home</div>
  <a class="abs nav-link" style="left:512px">About Us</a>
  <a class="abs nav-link" style="left:612px">New Release</a>
  <a class="abs nav-link" style="left:746px">Contact</a>
  <div class="abs social-square" aria-label="Social page link"></div>
  <div class="abs search">Search
    <svg width="14" height="14" viewBox="0 0 14 14"><circle cx="5.5" cy="5.5" r="4" fill="#d6ecfa" stroke="#3a7fc0" stroke-width="1.4"/><line x1="8.5" y1="8.5" x2="13" y2="13" stroke="#c9962a" stroke-width="2.2"/></svg>
  </div>
</header>

<section class="hero">
  <div class="abs hero-visual" role="img" aria-label="Laptop and tablet showing the Brindova name, surrounded by clouds"></div>
  <svg class="abs arrow" style="left:194px" width="26" height="40" viewBox="0 0 26 40"><path d="M20 3 L6 20 L20 37" fill="none" stroke="#777" stroke-width="6" stroke-linecap="round" stroke-linejoin="round"/></svg>
  <svg class="abs arrow" style="left:980px" width="26" height="40" viewBox="0 0 26 40"><path d="M6 3 L20 20 L6 37" fill="none" stroke="#777" stroke-width="6" stroke-linecap="round" stroke-linejoin="round"/></svg>
  <h1 class="abs hero-title">WHERE THERE IS BRINDOVA</h1>
  <p class="abs hero-sub">THERE’S YOUR WORKSPACE.</p>
  <p class="abs hero-copy">Curabitur suscipit quam sed neque molestie<br>Nec susipit ipsum hendrerit<br>Maecenas suscipit nulla in elit viverra vel<br>Vehicula nunc pellentesque</p>
  <a class="abs btn btn-large">
    <svg width="22" height="24" viewBox="0 0 22 24"><path d="M5 14 a5 5 0 0 1 1-9.8 a6 6 0 0 1 11 1.5 a4 4 0 0 1 0 8.3z" fill="#fff"/><path d="M11 12 v9 m-3-3 l3 3 l3-3" stroke="#2aa3e0" stroke-width="2" fill="none"/></svg>
    Read more</a>
  <div class="abs dots"><span class="dot active"></span><span class="dot"></span><span class="dot"></span><span class="dot"></span></div>
  <div class="abs band" style="top:556px"></div>
  <div class="abs band-line" style="top:615px"></div>
</section>

<section class="features">
  <div class="abs connector" style="left:410px;width:68px"></div>
  <div class="abs connector" style="left:715px;width:68px"></div>

  <h2 class="abs feature-title" style="left:176px">Bring your apps anywhere</h2>
  <div class="abs feature-frame" style="left:173px"><div class="feature-art" role="img" aria-label="Laptop with application and database icons"></div></div>
  <p class="abs feature-text" style="left:176px;top:832px">You can use your apps which you want on any computers anywhere.</p>

  <h2 class="abs feature-title" style="left:480px">Bring your config anywhere</h2>
  <div class="abs feature-frame" style="left:477px"><div class="feature-art" role="img" aria-label="Laptop with wrench and screwdriver"></div></div>
  <p class="abs feature-text" style="left:480px;top:823px">You can use your settings,<br>add-ins and so on which you have been used on any computer anywhere.</p>

  <h2 class="abs feature-title" style="left:785px">Share your apps friends</h2>
  <div class="abs feature-frame" style="left:782px"><div class="feature-art" role="img" aria-label="Group of user icons beside a settings gear"></div></div>
  <p class="abs feature-text" style="left:785px;top:823px">You can use your apps and settings including add-ins with your friend.</p>

  <a class="abs btn btn-small" style="left:334px"><svg width="11" height="11" viewBox="0 0 22 24"><path d="M5 14 a5 5 0 0 1 1-9.8 a6 6 0 0 1 11 1.5 a4 4 0 0 1 0 8.3z" fill="#fff"/></svg>Read more</a>
  <a class="abs btn btn-small" style="left:638px"><svg width="11" height="11" viewBox="0 0 22 24"><path d="M5 14 a5 5 0 0 1 1-9.8 a6 6 0 0 1 11 1.5 a4 4 0 0 1 0 8.3z" fill="#fff"/></svg>Read more</a>
  <a class="abs btn btn-small" style="left:942px"><svg width="11" height="11" viewBox="0 0 22 24"><path d="M5 14 a5 5 0 0 1 1-9.8 a6 6 0 0 1 11 1.5 a4 4 0 0 1 0 8.3z" fill="#fff"/></svg>Read more</a>

  <p class="abs lead">Lorem metus,&nbsp; volutpat orare molestie convallis, iaclis guis lectus. Ut varius risus eget neque tempus varius. Pellentesque sit amet m i vel quam dignis-sim convallis. Quisque elit quam, euismod nec convalis sed, lacils id est. Aloquam a lobirtis m i. Cras feugiat iaclis tellus, quis luctus nunc fermentum sit amet. Quisque lacina, lectus nec fermentum dictum.</p>
</section>

<footer>
  <div class="abs band-line" style="top:1053px"></div>
  <div class="abs band" style="top:1054px;transform:scaleY(-1)"></div>
  <p class="abs copyright">Copyright (C) Brindova Inc - 2012 All rights Reserved</p>
  <p class="abs footer-links">home .... about service .... about us ....contact us .... hiring<br>Blog / Testimonials / Sitemap</p>
</footer>

</body>
</html>
```